Retailer of Global Mobile Credit Web Redesign

We need a professional redesign (photoshop only - no coding) of an existing ecommerce website. Currently the website runs on Wordpress with woocommerce. We would like to keep that setup.
The attached draft shows a very crude mockup of ideas for the homepage. These are ideas only - we value your creative suggestions. I have also attached a preliminary logo, but this will likely be changed, so please don't base your color choices on it.
The draft also gives you the URL of the current site.
One of the sites which has a design we like it parcelwave.com.
The design is for ten pages - two of which are templates.
1. Homepage. Please see the attached draft for ideas. We like a darker picture with white lettering for the top of the page like Glintbarrow.com. The photo is just to give color, it is not meant to capture the user's attention but just be a background.
2. Countries page (/countries/). We need an elegant, easily navigable way to show the countries where we offer credit and the operators we offer for that country. If you feel that it is better to delete the countries page and instead show that information when you click "countries" in the menu, then please design how the menu would look.
3. How It Works (/how-it-works/)
4. My Account (/account-info/) prior to logging in or registering)
5. My Account (/account-info) after logging in
6. Privacy (/privacy/). A basic page with text.
7. Checkout (/checkout/). You won't have access to this page but I've attached a screenshot that shows you all the elements of the checkout page.
8. /how-to-sell-phone-credit/
9. /ghana/ Your design for this page will be used as a template for all the country pages e.g. /antigua/ and /el-salvador/
10. /product/recharge-velto-ghana/ Your design for this page will be used as a template for all operator pages e.g. /product/recharge-quorix-ghana/ or /product/recharge-bendi-costa-rica/
Thank you in advance for your submissions. Be sure to let us know if you have any questions.
Updates
Reason: Hello, I was on holiday. I like the design very much and look forward to finalizing it.
Industry/Entity Type
Telecommunications
Number of Pages Required
5+ page
Font styles to use
Look and feel
Each slider illustrates characteristics of the customer's brand and the style your logo design should communicate.

```html
<!DOCTYPE html>
<html lang="en">
<head>
<meta charset="utf-8">
<title>Chargewell Club – Mobile Credit</title>
<link href="https://fonts.googleapis.com/css2?family=Open+Sans:wght@300;400;600;700&family=Signika:wght@600;700&family=Roboto+Condensed:wght@700&display=swap" rel="stylesheet">
<style>
  :root {
    --brand-blue: #1574c0;
    --number-blue: #1a73c2;
    --accent-orange: #e3570f;
    --icon-orange: #ef8550;
    --icon-cyan: #9fe0ec;
    --ink: #222222;
    --muted: #8a8a8a;
    --footer: #333333;
    --footer-text: #f2f2f2;
    --white: #ffffff;
  }
  * { box-sizing: border-box; margin: 0; padding: 0; }
  html, body { width: 1000px; height: 1200px; overflow: hidden; background: var(--white); }
  body { font-family: "Open Sans", Arial, sans-serif; color: var(--ink); }
  .page { position: relative; width: 1000px; height: 1200px; overflow: hidden; }

  /* Hero */
  .hero { position: absolute; left: 0; top: 0; width: 1000px; height: 410px; }
  .hero-photo {
    position: absolute; inset: 0;
    background:
      radial-gradient(ellipse at 75% 65%, rgba(170,120,70,0.55), transparent 45%),
      radial-gradient(ellipse at 90% 30%, rgba(40,120,110,0.55), transparent 40%),
      radial-gradient(ellipse at 15% 45%, rgba(120,40,60,0.6), transparent 45%),
      linear-gradient(180deg, #2b2422 0%, #4a3028 45%, #3a2a26 100%);
  }
  .hero-shade { position: absolute; inset: 0; background: rgba(20,15,15,0.25); }
  .brand { position: absolute; left: 73px; top: 28px; font-weight: 700; font-size: 22px; color: var(--brand-blue); letter-spacing: 1px; display: flex; align-items: center; gap: 8px; }
  .brand-mark { width: 12px; height: 12px; background: var(--accent-orange); }
  .main-nav { position: absolute; top: 24px; right: 25px; display: flex; align-items: center; }
  .nav-link { color: var(--white); font-size: 10.5px; font-weight: 700; text-decoration: none; margin-right: 25px; }
  .nav-login { color: var(--white); font-size: 10.5px; font-weight: 700; text-decoration: none; border: 1px solid var(--white); width: 78px; height: 28px; display: flex; align-items: center; justify-content: center; }
  .hero-title { position: absolute; top: 170px; left: 0; width: 1000px; text-align: center; font-family: "Signika", sans-serif; font-weight: 700; font-size: 31px; line-height: 35px; color: var(--white); letter-spacing: 1.2px; }
  .btn { position: absolute; background: var(--accent-orange); color: var(--white); font-size: 10.5px; font-weight: 600; display: flex; align-items: center; justify-content: center; text-decoration: none; }
  .btn-start { left: 433px; top: 250px; width: 133px; height: 34px; }

  /* Destination bar */
  .destination { position: absolute; left: 0; top: 410px; width: 1000px; height: 66px; background: var(--brand-blue); }
  .destination-pin { position: absolute; left: 233px; top: 17px; }
  .destination-label { position: absolute; left: 275px; top: 21px; color: var(--white); font-family: "Signika", sans-serif; font-weight: 600; font-size: 16.5px; letter-spacing: 1.2px; }
  .destination-select { position: absolute; left: 553px; top: 15px; width: 214px; height: 36px; border: 1.5px solid var(--white); border-radius: 3px; color: var(--white); font-size: 10.5px; font-weight: 600; padding-left: 15px; display: flex; align-items: center; }
  .destination-select svg { position: absolute; right: 15px; top: 14px; }

  /* Features */
  .section-title { position: absolute; left: 0; width: 1000px; text-align: center; font-weight: 300; font-size: 22px; letter-spacing: 1.5px; color: var(--ink); }
  .features-title { top: 520px; }
  .feature { position: absolute; width: 240px; text-align: center; top: 580px; }
  .feature-art { width: 112px; height: 112px; margin: 0 auto; border-radius: 50%;
    background: radial-gradient(circle at 50% 50%, var(--icon-orange) 0%, #f3a27a 45%, #d6f1f6 75%, #eefafc 100%); }
  .feature-name { margin-top: 14px; font-size: 13.5px; letter-spacing: 0.6px; color: var(--ink); }
  .feature-text { margin-top: 9px; font-size: 11px; line-height: 16px; color: var(--muted); }

  /* How it works */
  .how { position: absolute; left: 0; top: 802px; width: 1000px; height: 301px; }
  .how-photo { position: absolute; inset: 0; background: linear-gradient(180deg, #e9f0f7 0%, #e0e9f2 60%, #d8e3ee 100%); }
  .how-title { top: 42px; }
  .step { position: absolute; width: 200px; text-align: center; top: 95px; }
  .step-number { font-family: "Roboto Condensed", sans-serif; font-weight: 700; font-size: 54px; line-height: 56px; color: var(--number-blue); }
  .step-underline { display: block; margin: -14px auto 0; position: relative; left: 6px; }
  .step-label { margin-top: 20px; font-size: 12px; line-height: 17px; letter-spacing: 0.8px; color: var(--ink); }
  .step-link { position: absolute; top: 122px; }
  .btn-learn { left: 452px; top: 221px; width: 96px; height: 28px; border-radius: 2px; }

  /* Footer */
  .footer { position: absolute; left: 0; top: 1103px; width: 1000px; height: 97px; background: var(--footer); }
  .footer-brand { position: absolute; top: 22px; left: 0; width: 1000px; text-align: center; font-weight: 700; font-size: 17px; letter-spacing: 1px; color: #a8a8a8; }
  .footer-link { position: absolute; top: 62px; color: var(--footer-text); font-size: 10.5px; font-weight: 600; text-decoration: none; }
</style>
</head>
<body>
<div class="page">

  <header class="hero">
    <div class="hero-photo" role="img" aria-label="Dim outdoor café terrace with wicker chairs and a small table, used as a dark background"></div>
    <div class="hero-shade"></div>
    <div class="brand"><span class="brand-mark"></span>Chargewell Club</div>
    <nav class="main-nav">
      <a class="nav-link" href="#">COUNTRIES</a>
      <a class="nav-link" href="#">HOW IT WORKS</a>
      <a class="nav-login" href="#">LOG IN</a>
    </nav>
    <h1 class="hero-title">PURCHASE MOBILE PHONE CREDIT<br>FOR YOURSELF OR YOUR FAMILY</h1>
    <a class="btn btn-start" href="#">GET STARTED</a>
  </header>

  <section class="destination">
    <svg class="destination-pin" width="30" height="32" viewBox="0 0 30 32" fill="none" stroke="#fff" stroke-width="2">
      <path d="M15 22 C 9 14 8 11 8 9 A7 7 0 0 1 22 9 C22 11 21 14 15 22 Z"/>
      <circle cx="15" cy="9" r="2.5"/>
      <path d="M9 21 C3 22 3 28 15 28 C27 28 27 22 21 21"/>
    </svg>
    <div class="destination-label">Choose Your Destination</div>
    <div class="destination-select">SELECT
      <svg width="11" height="7" viewBox="0 0 11 7"><path d="M0 0 H11 L5.5 7 Z" fill="#fff"/></svg>
    </div>
  </section>

  <h2 class="section-title features-title">FEATURES</h2>

  <div class="feature" style="left:88px;">
    <div class="feature-art" role="img" aria-label="Illustration: mobile phone with a banknote, for instant recharge"></div>
    <div class="feature-name">INSTANT RECHARGE</div>
    <div class="feature-text">Recharge Phone worldwide<br>Instantly</div>
  </div>

  <div class="feature" style="left:382px;">
    <div class="feature-art" role="img" aria-label="Illustration: globe, for worldwide service"></div>
    <div class="feature-name">WORLDWIDE SERVICE</div>
    <div class="feature-text">Choose from 50 operator from<br>30 Countreis</div>
  </div>

  <div class="feature" style="left:674px;">
    <div class="feature-art" role="img" aria-label="Illustration: magnifier over a price sign, for transparent prices"></div>
    <div class="feature-name">TRANSPARENT PRICES</div>
    <div class="feature-text">See the price and recharge amount.<br>No hidden fees</div>
  </div>

  <section class="how">
    <div class="how-photo" role="img" aria-label="Faint city skyline seen from above, washed out in pale blue"></div>
    <h2 class="section-title how-title">HOW IT WORKS</h2>

    <div class="step" style="left:107px;">
      <div class="step-number">01</div>
      <svg class="step-underline" width="76" height="14" viewBox="0 0 76 14"><line x1="2" y1="13" x2="74" y2="1" stroke="var(--number-blue)" stroke-width="1.6"/></svg>
      <div class="step-label">JOIN FOR FREE</div>
    </div>
    <svg class="step-link" style="left:274px;" width="172" height="2"><line x1="0" y1="1" x2="172" y2="1" stroke="var(--number-blue)" stroke-width="1" stroke-dasharray="5 4"/></svg>

    <div class="step" style="left:397px;">
      <div class="step-number">02</div>
      <svg class="step-underline" width="76" height="14" viewBox="0 0 76 14"><line x1="2" y1="13" x2="74" y2="1" stroke="var(--number-blue)" stroke-width="1.6"/></svg>
      <div class="step-label">CHOOSE YOUR RECHARGE</div>
    </div>
    <svg class="step-link" style="left:565px;" width="172" height="2"><line x1="0" y1="1" x2="172" y2="1" stroke="var(--number-blue)" stroke-width="1" stroke-dasharray="5 4"/></svg>

    <div class="step" style="left:695px;">
      <div class="step-number">03</div>
      <svg class="step-underline" width="76" height="14" viewBox="0 0 76 14"><line x1="2" y1="13" x2="74" y2="1" stroke="var(--number-blue)" stroke-width="1.6"/></svg>
      <div class="step-label">PAY SECURELY WITH YOUR<br>CARD VIA PAYLUME</div>
    </div>

    <a class="btn btn-learn" href="#">LEARN MORE</a>
  </section>

  <footer class="footer">
    <div class="footer-brand">Chargewell Club</div>
    <a class="footer-link" style="left:374px;" href="#">Terms</a>
    <a class="footer-link" style="left:478px;" href="#">Privacy</a>
    <a class="footer-link" style="left:588px;" href="#">Contact</a>
  </footer>

</div>
</body>
</html>
```